Solar appointment reminder card

We are looking for a new design for our appointment reminder card since we have changed our logo. The card should have the new logo along with space for the employee to hand write the customers appointment date, time, the employees name and phone number.
I've uploaded what our old basic appointment card looked like and our new logo.

The cards should be in a standard business card size and could be horizontal or vertical.

```html
<!DOCTYPE html>
<html lang="en">
<head>
<meta charset="utf-8">
<title>Appointment Reminder Card – Two Versions</title>
<link href="https://fonts.googleapis.com/css2?family=Cinzel:wght@400;600&family=PT+Serif:wght@400;700&display=swap" rel="stylesheet">
<style>
  :root {
    --bg-dark: #2b2b2b;
    --bg-mid: #4a4a4a;
    --card: #eeeeee;
    --ink: #2a2a2a;
    --rule: #8a8a8a;
    --orange: #f7931e;
    --sun-yellow: #fcc321;
    --gold: #f2b415;
    --white: #ffffff;
  }
  * { box-sizing: border-box; margin: 0; padding: 0; }
  html, body { width: 905px; height: 1200px; overflow: hidden; }
  body {
    background: radial-gradient(ellipse at 50% 30%, var(--bg-mid) 0%, var(--bg-dark) 75%);
    font-family: "PT Serif", Georgia, serif;
    position: relative;
  }
  .version-label {
    position: absolute;
    left: 106px;
    color: var(--white);
    font-family: "PT Serif", Georgia, serif;
    font-size: 40px;
    letter-spacing: 4px;
  }
  .version-label.v1 { top: 42px; }
  .version-label.v2 { top: 640px; }

  .card {
    position: absolute;
    left: 172px;
    width: 560px;
    height: 320px;
    background: var(--card);
    overflow: hidden;
    box-shadow: 0 14px 30px rgba(0,0,0,0.45);
  }
  .card.v1 { top: 140px; }
  .card.v2 { top: 740px; }
  .card-art { position: absolute; inset: 0; }

  .appointment-block { position: absolute; }
  .appointment-title {
    font-family: "Cinzel", serif;
    font-size: 20px;
    letter-spacing: 1px;
    white-space: nowrap;
    padding: 6px 0 4px;
    border-top: 2px dotted var(--rule);
    border-bottom: 2px dotted var(--rule);
  }
  .field {
    position: absolute;
    font-family: "PT Serif", Georgia, serif;
    font-weight: 700;
    font-size: 15px;
    color: var(--ink);
    white-space: nowrap;
  }

  .brand {
    position: absolute;
    font-family: "PT Serif", Georgia, serif;
    font-weight: 700;
    line-height: 1;
  }
  .brand-name { font-size: 42px; letter-spacing: 2px; display: block; }
  .brand-tagline { font-size: 12px; letter-spacing: 2px; display: block; margin-top: 4px; text-transform: uppercase; }

  /* Version 1 */
  .v1 .appointment-block { left: 38px; top: 58px; width: 180px; }
  .v1 .appointment-title { color: var(--ink); }
  .v1 .field.date  { left: 60px; top: 130px; }
  .v1 .field.time  { left: 60px; top: 164px; }
  .v1 .field.rep   { left: 60px; top: 198px; }
  .v1 .field.phone { left: 60px; top: 232px; }
  .v1 .brand {
    left: 360px; top: 88px;
    width: 190px;
    text-align: center;
    color: var(--white);
  }

  /* Version 2 */
  .v2 .brand { left: 40px; top: 44px; color: var(--orange); }
  .v2 .appointment-block { left: 78px; top: 138px; width: 176px; }
  .v2 .appointment-title { color: var(--gold); }
  .v2 .field.date  { left: 100px; top: 216px; }
  .v2 .field.time  { left: 112px; top: 252px; }
  .v2 .field.rep   { left: 290px; top: 150px; }
  .v2 .field.phone { left: 304px; top: 184px; }
</style>
</head>
<body>

  <div class="version-label v1">V 1</div>

  <section class="card v1" aria-label="Appointment card, version one">
    <svg class="card-art" viewBox="0 0 560 320" width="560" height="320">
      <path role="img" aria-label="Sun burst illustration behind the brand circle"
            d="M170 0 L560 0 L560 320 L300 320 C260 240 200 120 170 0 Z"
            fill="var(--sun-yellow)"/>
      <circle cx="460" cy="110" r="165" fill="var(--orange)"/>
    </svg>

    <div class="appointment-block"><div class="appointment-title">Appointment</div></div>
    <div class="field date">Date :</div>
    <div class="field time">Time :</div>
    <div class="field rep">Representative:</div>
    <div class="field phone">Phone:</div>

    <div class="brand">
      <span class="brand-name">KSP</span>
      <span class="brand-tagline">Keystone Sun Power</span>
    </div>
  </section>

  <div class="version-label v2">V 2</div>

  <section class="card v2" aria-label="Appointment card, version two">
    <svg class="card-art" viewBox="0 0 560 320" width="560" height="320">
      <defs>
        <linearGradient id="landmark-fill" x1="0" y1="0" x2="1" y2="0">
          <stop offset="0" stop-color="#ffffff"/>
          <stop offset="1" stop-color="#f7931e"/>
        </linearGradient>
      </defs>
      <rect role="img" aria-label="Landmark silhouette illustration in white on orange"
            x="420" y="0" width="140" height="320" fill="url(#landmark-fill)"/>
    </svg>

    <div class="brand">
      <span class="brand-name">KSP</span>
      <span class="brand-tagline">Keystone Sun Power</span>
    </div>

    <div class="appointment-block"><div class="appointment-title">Appointment</div></div>
    <div class="field rep">Representative:</div>
    <div class="field phone">Phone:</div>
    <div class="field date">Date :</div>
    <div class="field time">Time :</div>
  </section>

</body>
</html>
```